Need Business Cards for my Business

email address: rkpmarlowhollowworks@vendrimail.com
web address: rkpmarlowhollowworks.net
Slogan: We offer various QVN licenses
Rowland K. Pemberly
Please stick with colors of Company Logo
would like the card to be more of the color example of the logo.
If you need PDF copy of logo email me at the above account.
Creative control rests with you.

Industry/Entity Type

Business

Contact Information for Business Card

I am a minimalist, but would like something to pop and stand out amongst other cards, make it memorable.

Font styles to use
Serif
Decorative
Script

```html
<!DOCTYPE html>
<html lang="en">
<head>
<meta charset="utf-8">
<title>RKP Marlow Hollow – Business Cards</title>
<link rel="stylesheet" href="https://fonts.googleapis.com/css2?family=Arimo:wght@400;700&display=swap">
<style>
  :root {
    --navy: #173a63;
    --navy-deep: #12314f;
    --red: #e0262f;
    --white: #f4f5f6;
    --ink: #0c0c0c;
    --backdrop: #e6e2dc;
    --text-light: #eef2f7;
  }
  * { box-sizing: border-box; margin: 0; padding: 0; }
  html, body { width: 1200px; height: 902px; overflow: hidden; }
  body {
    background: var(--backdrop);
    font-family: "Arimo", Arial, sans-serif;
    position: relative;
  }
  .card {
    position: absolute;
    left: 260px;
    width: 680px;
    height: 389px;
    background: var(--white);
    overflow: hidden;
    box-shadow: 0 6px 18px rgba(0,0,0,.18);
  }
  .card--back { top: 40px; }
  .card--front { top: 473px; }

  /* back side */
  .band { position: absolute; left: 0; right: 0; background: var(--navy); }
  .band--top { top: 0; height: 92px; }
  .band--bottom { bottom: 0; height: 92px; }

  .brand {
    position: absolute;
    display: flex;
    align-items: center;
    gap: 16px;
  }
  .brand__dot {
    width: 34px; height: 34px;
    border-radius: 50%;
    background: var(--red);
    flex: none;
  }
  .brand__name {
    font-weight: 700;
    font-size: 40px;
    letter-spacing: 1px;
    color: var(--navy);
    text-transform: uppercase;
    line-height: 1;
    white-space: nowrap;
  }
  .card--back .brand { left: 110px; top: 150px; }
  .slogan {
    position: absolute;
    left: 160px; top: 222px;
    color: var(--red);
    font-size: 20px;
    letter-spacing: 3px;
  }

  /* front side */
  .card--front .brand { left: 96px; top: 100px; }
  .rule-black {
    position: absolute; left: 0; right: 0; top: 206px;
    height: 14px; background: var(--ink);
  }
  .contact-panel {
    position: absolute; left: 0; right: 0; top: 220px; bottom: 0;
    background: var(--navy);
  }
  .contact-list {
    position: absolute;
    right: 304px; top: 26px;
    list-style: none;
    display: flex; flex-direction: column; gap: 12px;
    align-items: flex-end;
  }
  .contact-list li {
    display: flex; align-items: center; gap: 12px;
    color: var(--text-light);
    font-size: 17px;
    white-space: nowrap;
  }
  .icon {
    width: 22px; height: 22px;
    background: var(--text-light);
    border-radius: 3px;
    display: flex; align-items: center; justify-content: center;
    flex: none;
  }
  .divider {
    position: absolute; left: 394px; top: 18px;
    width: 2px; height: 122px;
    background: var(--text-light);
  }
  .holder-name {
    position: absolute; left: 418px; right: 30px; top: 64px;
    color: var(--text-light);
    font-size: 24px;
    white-space: nowrap;
  }
</style>
</head>
<body>

<section class="card card--back" aria-label="Card back">
  <div class="band band--top"></div>
  <div class="brand">
    <span class="brand__dot"></span>
    <span class="brand__name">RKP Marlow Hollow</span>
  </div>
  <p class="slogan">We offer various QVN licenses</p>
  <div class="band band--bottom"></div>
</section>

<section class="card card--front" aria-label="Card front">
  <div class="brand">
    <span class="brand__dot"></span>
    <span class="brand__name">RKP Marlow Hollow</span>
  </div>
  <div class="rule-black"></div>
  <div class="contact-panel">
    <ul class="contact-list">
      <li>555-014-2290
        <span class="icon">
          <svg width="14" height="14" viewBox="0 0 24 24"><path fill="#173a63" d="M6.6 10.8a15 15 0 0 0 6.6 6.6l2.2-2.2a1 1 0 0 1 1-.25 11.4 11.4 0 0 0 3.6.6 1 1 0 0 1 1 1V20a1 1 0 0 1-1 1A17 17 0 0 1 3 4a1 1 0 0 1 1-1h3.5a1 1 0 0 1 1 1c0 1.25.2 2.45.6 3.6a1 1 0 0 1-.25 1z"/></svg>
        </span>
      </li>
      <li>rkpmarlowhollowworks.net
        <span class="icon">
          <svg width="14" height="14" viewBox="0 0 24 24" fill="none" stroke="#173a63" stroke-width="2"><circle cx="12" cy="12" r="9"/><path d="M3 12h18M12 3c3 3 3 15 0 18M12 3c-3 3-3 15 0 18"/></svg>
        </span>
      </li>
      <li>rkpmarlowhollowworks@vendrimail.com
        <span class="icon">
          <svg width="14" height="14" viewBox="0 0 24 24" fill="none" stroke="#173a63" stroke-width="2"><rect x="3" y="6" width="18" height="12"/><path d="M3 6l9 7 9-7"/></svg>
        </span>
      </li>
    </ul>
    <div class="divider"></div>
    <p class="holder-name">Rowland K. Pemberly</p>
  </div>
</section>

</body>
</html>
```